Modern HomePage Design for Church

We are looking for a modern homepage design using the sections we put together in the template. The colors we want are blue, black, grey, and white. We do not want use the colors in the logo. Please modify the logo color to match the website color scheme.

Target Market(s)

Church

Industry/Entity Type

Church

Number of Pages Required

1 page

Colors
0293ce
ffffff
474747
9d9d9d

```html
<!DOCTYPE html>
<html lang="en">
<head>
<meta charset="utf-8">
<title>Wellspring Grace Community Church</title>
<link rel="stylesheet" href="https://fonts.googleapis.com/css2?family=Montserrat:ital,wght@0,400;0,500;0,600;0,700;1,400;1,600&family=Open+Sans:wght@400;600&display=swap">
<style>
:root{
  --blue:#0293ce;
  --white:#ffffff;
  --dark:#474747;
  --grey:#9d9d9d;
  --black:#0f0f0f;
  --ink:#222222;
  --footer:#1b1b1b;
}
*{box-sizing:border-box;margin:0;padding:0}
html,body{width:1200px;height:4063px;overflow:hidden;background:var(--white)}
body{font-family:"Open Sans",sans-serif;color:var(--ink)}
.page{position:relative;width:1200px;height:4063px;overflow:hidden}
.abs{position:absolute}
.head{font-family:"Montserrat",sans-serif}
.btn{position:absolute;display:flex;align-items:center;justify-content:center;font-family:"Montserrat",sans-serif;text-transform:uppercase;letter-spacing:.5px}
.photo{position:absolute}

/* nav */
.nav{top:0;left:0;width:1200px;height:49px;background:var(--white)}
.nav-brand{left:78px;top:10px;font-family:"Montserrat",sans-serif;font-size:11px;font-weight:600;color:var(--dark);line-height:13px;text-transform:uppercase;display:flex;align-items:center;gap:6px}
.nav-brand .dot{width:14px;height:14px;border-radius:50%;background:var(--blue)}
.nav-links{left:292px;top:0;height:49px;display:flex;align-items:center;gap:36px;font-family:"Montserrat",sans-serif;font-size:13px;color:#555;text-transform:uppercase}
.give{left:1002px;top:5px;width:122px;height:36px;background:var(--blue);color:var(--white);font-size:13px;font-weight:600}

/* hero */
.hero{top:49px;left:0;width:1200px;height:593px;background:linear-gradient(180deg,#0e1a26 0%,#2a2f38 35%,#8a5a2e 58%,#d98a3a 66%,#1a1410 75%,#050505 100%)}
.hero-title{left:200px;top:280px;width:800px;text-align:center;color:var(--white);font-family:"Montserrat",sans-serif;font-weight:600;font-size:28px;line-height:42px}
.explore{left:490px;top:406px;width:230px;height:55px;border:2px solid var(--white);color:var(--white);font-size:24px;font-weight:600}

/* visitor band */
.band{top:642px;left:0;width:1200px;height:84px;background:var(--blue)}
.band-text{left:68px;top:672px;color:var(--white);font-family:"Montserrat",sans-serif;font-size:17px}
.visitors{left:783px;top:656px;width:190px;height:54px;border-radius:27px;background:var(--white);color:var(--blue);font-size:14px;font-weight:600}

/* welcome */
.welcome-title{left:54px;top:803px;font-family:"Montserrat",sans-serif;font-size:17px;font-weight:500;color:#666;letter-spacing:1px;text-transform:uppercase}
.welcome-text{left:54px;top:858px;width:612px;font-size:14.5px;line-height:25.5px;color:var(--grey)}
.welcome-photo{left:664px;top:726px;width:536px;height:439px;background:linear-gradient(160deg,#f0f1ee 0%,#c9d1c4 45%,#6f8a4c 75%,#3e5530 100%)}

/* event */
.event{top:1165px;left:0;width:1200px;height:244px;background:var(--black)}
.event-title{left:172px;top:1199px;width:400px;text-align:center;color:var(--white);font-family:"Montserrat",sans-serif;font-size:22px;font-weight:500}
.event-date{left:172px;top:1234px;width:400px;text-align:center;color:var(--grey);font-family:"Montserrat",sans-serif;font-size:15px;letter-spacing:1px}
.event-text{left:172px;top:1260px;width:400px;text-align:center;color:var(--white);font-size:13.5px;line-height:24px}
.event-btn{left:309px;top:1333px;width:143px;height:38px;background:var(--blue);color:var(--white);font-size:13px;font-weight:600}
.count{position:absolute;top:1235px;width:66px;text-align:center}
.count .num{width:66px;height:66px;border-radius:50%;background:#2f2f2f;color:var(--white);font-family:"Montserrat",sans-serif;font-weight:700;font-size:22px;display:flex;align-items:center;justify-content:center}
.count .lbl{margin-top:16px;color:var(--grey);font-size:14px}

/* features */
.feature{position:absolute;top:1480px;width:360px;text-align:left}
.feature svg{display:block;margin:0 auto 14px}
.feature h3{font-family:"Montserrat",sans-serif;font-size:19px;font-weight:700;color:var(--ink);text-align:center;text-transform:uppercase;letter-spacing:.5px;margin-bottom:16px}
.feature p{font-size:14px;line-height:24px;color:#555;padding:0 2px}
.feature .more{position:absolute;left:0;top:295px;width:178px;height:48px;border:1.5px solid var(--grey);color:#555;font-size:14px}

/* ministries */
.cell{position:absolute}
.tag{position:absolute;border:1.5px solid var(--white);color:var(--white);font-family:"Montserrat",sans-serif;font-size:12px;display:flex;align-items:center;justify-content:center;text-transform:uppercase;letter-spacing:1px;background:rgba(0,0,0,.25)}
.involved-dark{top:1910px;left:759px;width:441px;height:360px;background:#3b3b3b}
.involved-grey{top:2270px;left:0;width:439px;height:358px;background:var(--dark)}
.h-involved{font-family:"Montserrat",sans-serif;font-size:31px;font-weight:600;color:var(--white)}
.p-involved{font-size:15px;line-height:27px;color:var(--white)}
.pray-title{left:439px;top:2343px;width:761px;text-align:center;font-family:"Montserrat",sans-serif;font-size:34px;font-weight:500;color:var(--ink)}
.pray-line{left:965px;top:2395px;width:55px;height:5px;background:var(--blue)}
.pray-text{left:490px;top:2448px;width:665px;font-size:16px;line-height:26px;color:var(--grey)}
.pray-btn{left:731px;top:2533px;width:179px;height:46px;background:var(--blue);color:var(--white);font-size:15px;font-weight:600}

/* sermons */
.sermons{top:2628px;left:0;width:1200px;height:365px;background:linear-gradient(90deg,#1a1a1a 0%,#2a2a2a 55%,#1c1c1c 100%)}
.pastor{left:45px;top:2684px;width:250px;height:250px;border-radius:50%;background:linear-gradient(180deg,#d8dde2 0%,#9aa4ae 55%,#2f3a4a 100%);border:4px solid #3a3a3a}
.quote{left:330px;top:2684px;width:290px;color:var(--white);font-family:"Montserrat",sans-serif;font-size:25px;font-weight:700;line-height:34px}
.quote-text{left:330px;top:2778px;width:320px;color:#e6e6e6;font-size:14px;line-height:24px}
.track{position:absolute;left:699px;display:flex;align-items:center;gap:20px}
.track .play{width:48px;height:48px;border-radius:50%;border:2px solid var(--white);display:flex;align-items:center;justify-content:center}
.track h4{font-family:"Montserrat",sans-serif;font-size:16px;font-weight:700;color:var(--white);text-transform:uppercase}
.track span{display:block;margin-top:6px;font-family:"Montserrat",sans-serif;font-style:italic;font-weight:600;font-size:15px;color:var(--blue)}

/* events */
.events-title{left:0;top:3060px;width:1200px;text-align:center;font-family:"Montserrat",sans-serif;font-size:30px;font-weight:700;color:var(--ink);letter-spacing:.5px}
.events-sub{left:0;top:3109px;width:1200px;text-align:center;font-family:"Montserrat",sans-serif;font-style:italic;font-size:15px;color:#444}
.card{position:absolute;top:3175px;width:324px;height:401px;background:var(--white);box-shadow:0 4px 16px rgba(0,0,0,.14)}
.card .img{height:165px}
.card h5{margin:30px 30px 0;font-family:"Montserrat",sans-serif;font-size:21px;font-weight:700;line-height:28px;color:var(--ink)}
.card p{margin:14px 30px 0;font-size:13.5px;line-height:22px;color:#555}
.card .more{position:absolute;left:99px;top:341px;width:126px;height:36px;border:1.5px solid #777;color:#444;font-size:11px}

/* footer */
.footer{top:3679px;left:0;width:1200px;height:317px;background:var(--footer)}
.foot-brand{left:81px;top:3800px;width:260px;color:var(--blue);font-family:"Montserrat",sans-serif;font-weight:500;font-size:30px;line-height:34px;text-align:center}
.foot-brand small{display:block;font-size:11px;line-height:16px;letter-spacing:1px;text-transform:uppercase}
.foot-col{position:absolute;top:3740px}
.foot-col h6{font-family:"Montserrat",sans-serif;font-size:20px;font-weight:600;color:var(--blue);text-transform:uppercase;letter-spacing:.5px;margin-bottom:14px}
.foot-col ul{list-style:none}
.foot-col li{font-size:15.5px;line-height:36.5px;color:#cfcfcf}
.foot-col address{font-style:normal;font-size:13px;line-height:24px;color:#cfcfcf}
.bottom{top:3996px;left:0;width:1200px;height:67px;background:#121212;border-top:1px solid #2c2c2c}
.social{position:absolute;top:4015px;width:32px;height:32px;border-radius:50%;background:var(--blue)}
</style>
</head>
<body>
<div class="page">

  <!-- navigation -->
  <header class="abs nav">
    <div class="abs nav-brand"><span class="dot"></span><span>Wellspring<br>Grace</span></div>
    <nav class="abs nav-links"><span>Home</span><span>Team</span><span>Features</span><span>Sermons</span><span>Events</span><span>Contact</span><span>Blog</span></nav>
    <div class="btn give">Give Now</div>
  </header>

  <!-- hero -->
  <section class="abs hero" role="img" aria-label="Silhouette of three crosses on a hill at sunset"></section>
  <h1 class="abs hero-title">Lorem ipsum dolor sit amet, consectetur adipiscing elit. Quisque tincidunt ligula id lorem male</h1>
  <div class="btn explore">Explore</div>

  <!-- visitor band -->
  <div class="abs band"></div>
  <p class="abs band-text">Lorem ipsum dolor sit amet, consectetur adipiscing elit. Quisque tincidunt</p>
  <div class="btn visitors">Visitors Info</div>

  <!-- welcome -->
  <h2 class="abs welcome-title">Welcome to Wellspring Grace Community Church</h2>
  <p class="abs welcome-text">Lorem ipsum dolor sit amet, consectetur adipiscing elit. Quisque tincidunt ligula id lorem malesuada mollis sed in augue. Nulla facilisi. Maecenas quis elit eu urna suscipit placerat. Integer iaculis et diam sit amet finibus. Pellentesque fermentum convallis nibh. Cras ullamcorper diam quis massa sollicitudin, et consequat nibh scelerisque. Proin vel erat metus. Morbi quam magna, vestibulum id egestas et, iaculis sed orci. Pellentesque et lectus tempus nibh</p>
  <div class="photo welcome-photo" role="img" aria-label="Smiling older couple embracing outdoors"></div>

  <!-- next event -->
  <section class="abs event"></section>
  <h3 class="abs event-title">Church Leaders Meeting</h3>
  <p class="abs event-date">May 20, 2019</p>
  <p class="abs event-text">Lorem ipsum dolor sit amet, consectetur adipiscing elit. Phasellus a dolor ut nibh consectetur porta.</p>
  <div class="btn event-btn">Read More</div>
  <div class="count" style="left:687px"><div class="num">06</div><div class="lbl">Days</div></div>
  <div class="count" style="left:785px"><div class="num">15</div><div class="lbl">Hours</div></div>
  <div class="count" style="left:885px"><div class="num">28</div><div class="lbl">Mins</div></div>
  <div class="count" style="left:978px"><div class="num">16</div><div class="lbl">Secs</div></div>

  <!-- features -->
  <div class="feature" style="left:38px">
    <svg width="60" height="56" viewBox="0 0 60 56"><path d="M30 52 C12 38 3 28 3 17 C3 8 10 3 17 3 C23 3 27 7 30 11 C33 7 37 3 43 3 C50 3 57 8 57 17 C57 28 48 38 30 52Z" fill="var(--blue)"/><polyline points="6,26 20,26 25,16 31,36 36,22 40,26 54,26" fill="none" stroke="#fff" stroke-width="3.5" stroke-linejoin="round"/></svg>
    <h3>What We Believe?</h3>
    <p>Lorem ipsum dolor sit amet, consectetur adipiscing elit. Phasellus a dolor ut nibh consectetur porta. Cras arcu nisl, ultrices nec dui feugiat, congue malesuada magna</p>
    <div class="btn more">Read More</div>
  </div>
  <div class="feature" style="left:398px">
    <svg width="60" height="56" viewBox="0 0 60 56"><circle cx="30" cy="28" r="24" fill="none" stroke="var(--blue)" stroke-width="4"/><polyline points="30,13 30,29 40,35" fill="none" stroke="var(--blue)" stroke-width="4" stroke-linecap="round"/></svg>
    <h3>Services &amp; Location</h3>
    <p>Lorem ipsum dolor sit amet, consectetur adipiscing elit. Phasellus a dolor ut nibh consectetur porta. Cras arcu nisl, ultrices nec dui feugiat, congue malesuada magna</p>
    <div class="btn more">Read More</div>
  </div>
  <div class="feature" style="left:760px">
    <svg width="64" height="56" viewBox="0 0 64 56"><path d="M38 26 C28 18 24 13 24 8 C24 4 27 2 30 2 C33 2 35 4 38 7 C41 4 43 2 46 2 C49 2 52 4 52 8 C52 13 48 18 38 26Z" fill="var(--blue)"/><path d="M4 38 L16 34 C22 32 28 34 34 36 L44 36 C47 36 47 41 44 41 L32 41 L48 41 L58 34 C61 32 63 36 61 38 L50 48 L22 50 L4 50Z" fill="var(--blue)"/></svg>
    <h3>Gifts and Donations</h3>
    <p>Lorem ipsum dolor sit amet, consectetur adipiscing elit. Phasellus a dolor ut nibh consectetur porta. Cras arcu nisl, ultrices nec dui feugiat, congue malesuada magna</p>
    <div class="btn more">Read More</div>
  </div>

  <!-- ministries -->
  <div class="cell" style="left:0;top:1910px;width:377px;height:182px;background:linear-gradient(135deg,#6b6f78,#a46a5a 55%,#3c3f46)" role="img" aria-label="Two young children in winter coats"></div>
  <div class="cell" style="left:377px;top:1910px;width:192px;height:182px;background:linear-gradient(135deg,#2f2f35,#5a4a44 60%,#26262a)" role="img" aria-label="Outreach volunteers holding signs"></div>
  <div class="cell" style="left:569px;top:1910px;width:190px;height:182px;background:linear-gradient(160deg,#e9e6df,#8a9b6a 60%,#5a6e3e)" role="img" aria-label="Friends sitting together on the grass"></div>
  <div class="cell" style="left:0;top:2092px;width:190px;height:178px;background:linear-gradient(135deg,#3a3636,#6f6055 60%,#2a2626)" role="img" aria-label="Senior members in fellowship"></div>
  <div class="cell" style="left:190px;top:2092px;width:187px;height:178px;background:linear-gradient(135deg,#5a4d44,#c9bba6 55%,#6e5e50)" role="img" aria-label="Open Bible on a table"></div>
  <div class="cell" style="left:377px;top:2092px;width:382px;height:178px;background:linear-gradient(135deg,#2c2c30,#4a403c 55%,#232326)" role="img" aria-label="Children at a kids ministry gathering"></div>
  <div class="tag" style="left:414px;top:1997px;width:112px;height:23px">Outreach</div>
  <div class="tag" style="left:41px;top:2170px;width:90px;height:23px">Senior</div>
  <div class="tag" style="left:482px;top:2167px;width:176px;height:33px">Kids Ministry</div>

  <div class="abs involved-dark"></div>
  <h3 class="abs h-involved" style="left:859px;top:1990px">Get involved</h3>
  <p class="abs p-involved" style="left:802px;top:2050px;width:372px">Lorem ipsum dolor sit amet, consectetur adipiscing elit. Phasellus a dolor ut nibh consectetur porta. Cras arcu nisl, ultrices nec dui feugiat congue malesuada</p>

  <div class="abs involved-grey"></div>
  <h3 class="abs h-involved" style="left:106px;top:2346px">Get involved</h3>
  <p class="abs p-involved" style="left:41px;top:2410px;width:360px">Lorem ipsum dolor sit amet, consectetur adipiscing elit. Phasellus a dolor ut nibh consectetur porta. Cras arcu nisl, ultrices nec dui feugiat congue malesuada</p>

  <h2 class="abs pray-title">Pray without ceasing</h2>
  <div class="abs pray-line"></div>
  <p class="abs pray-text">Lorem ipsum dolor sit amet, consectetur adipiscing elit. Quisque at congue nisi. Aliquam bibendum sodales quam, dapibus tempus lacus. Duis sed feugiat odio, sit amet ultrices est</p>
  <div class="btn pray-btn">Read More</div>

  <!-- sermons -->
  <section class="abs sermons"></section>
  <div class="abs pastor" role="img" aria-label="Portrait of the senior pastor in a suit"></div>
  <h3 class="abs quote">“Lorem ipsum dolor sit amet, consectetur”</h3>
  <p class="abs quote-text">Lorem ipsum dolor sit amet, consectetur adipiscing elit. Quisque at congue nisi. Aliquam bibendum sodales quam, dapibus tempus lacus. Duis sed feugiat odio, sit amet ultrices est</p>
  <div class="track" style="top:2692px"><div class="play"><svg width="16" height="18" viewBox="0 0 16 18"><path d="M3 1 L15 9 L3 17Z" fill="#fff"/></svg></div><div><h4>Holy Spirit: Strategic Thinking</h4><span>By Ruth Calloway</span></div></div>
  <div class="track" style="top:2774px"><div class="play"><svg width="16" height="18" viewBox="0 0 16 18"><path d="M3 1 L15 9 L3 17Z" fill="#fff"/></svg></div><div><h4>Holy Spirit: Strategic Thinking</h4><span>By Ruth Calloway</span></div></div>
  <div class="track" style="top:2862px"><div class="play"><svg width="16" height="18" viewBox="0 0 16 18"><path d="M3 1 L15 9 L3 17Z" fill="#fff"/></svg></div><div><h4>Holy Spirit: Strategic Thinking</h4><span>By Ruth Calloway</span></div></div>

  <!-- upcoming events -->
  <h2 class="abs events-title">UPCOMING EVENTS</h2>
  <p class="abs events-sub">Experiencing God’s presence</p>
  <article class="card" style="left:79px">
    <div class="img" style="background:linear-gradient(135deg,#c98a4a,#8a5a3a 50%,#e0b070)" role="img" aria-label="Three smiling children sitting together"></div>
    <h5>Lorem ipsum dolor sit amet</h5>
    <p>Lorem ipsum dolor sit amet, consectetur adipiscing elit. Duis posuere diam sed malesuada</p>
    <div class="btn more">Read More</div>
  </article>
  <article class="card" style="left:438px">
    <div class="img" style="background:linear-gradient(180deg,#2a2320,#7a5a3a 55%,#3a2c24)" role="img" aria-label="Interior of a church sanctuary with arches"></div>
    <h5>Lorem ipsum dolor sit amet</h5>
    <p>Lorem ipsum dolor sit amet, consectetur adipiscing elit. Duis posuere diam sed malesuada</p>
    <div class="btn more">Read More</div>
  </article>
  <article class="card" style="left:798px">
    <div class="img" style="background:linear-gradient(180deg,#cfc7a8,#6f8a4a 50%,#4a5a3a)" role="img" aria-label="Crowd gathered at an outdoor service in a park"></div>
    <h5>Lorem ipsum dolor sit amet</h5>
    <p>Lorem ipsum dolor sit amet, consectetur adipiscing elit. Duis posuere diam sed malesuada</p>
    <div class="btn more">Read More</div>
  </article>

  <!-- footer -->
  <footer class="abs footer"></footer>
  <div class="abs foot-brand">WELLSPRING<small>Grace Community Church</small></div>
  <div class="foot-col" style="left:434px"><h6>Quick Links</h6><ul><li>Home</li><li>About Us</li><li>Our Programs</li><li>Our Blogs</li></ul></div>
  <div class="foot-col" style="left:675px"><h6>Resources</h6><ul><li>Home</li><li>About Us</li><li>Our Services</li><li>Our Blogs</li></ul></div>
  <div class="foot-col" style="left:888px"><h6>Contact Us</h6><address>Suite 12, 48 Elmstead Lane<br>Bristol<br>England<br>hello@wellspringgrace.org</address></div>
  <div class="abs bottom"></div>
  <span class="social" style="left:883px" aria-label="Social link"></span>
  <span class="social" style="left:935px" aria-label="Social link"></span>
  <span class="social" style="left:992px" aria-label="Social link"></span>
  <span class="social" style="left:1049px" aria-label="Social link"></span>

</div>
</body>
</html>
```